New Business Card Design Project

Make a kick ass business card for The Otter Tea Mug, using the designs. I also might like the 2nd place design logo on the back? Maybe all black with that? Not sure. Also, I'm cool with it being on metal, plastic, glass? or whatever for the business card. Maybe shaped like a shark? Let me know what else you need? Would like designs in the next day or so. Thank you.
Target Market(s)
Anyone that is cool
Contact Information for Business Card
Name: Dorian Fenwick
Phone: 317.594.8126
inventor/creator/entrepreneur/owner
www.theottertyeamug.example
social media links
https://www.facebook.com/theottertyeamug
https://twitter.com/otter_brew
https://www.instagram.com/theottertyeamug/
I'll get the Pinterest one soon
Colors
Designer to choose colors to be used in the design.
Requirements
Must have
- The Otter Tea Mug
- www.theottertyeamug.example
- social media tags?
- My logos and picture/photo of wine glass
Nice to have
- Maybe shaped like a wine glass or shark
- I'll let you decide but my same colors from my website would be nice

```html
<!DOCTYPE html>
<html lang="en">
<head>
<meta charset="utf-8">
<title>Otter Tea Mug – Business Card</title>
<link rel="stylesheet" href="https://fonts.googleapis.com/css2?family=Montserrat:wght@500;600;700&family=Quicksand:wght@400;500&display=swap">
<style>
  :root {
    --card-red: #b94249;
    --card-white: #ffffff;
    --blush: #f6b8c2;
    --logo-grey: #6b6b6b;
    --page-bg: #ece6e3;
    --mark-deep: #8e1f2e;
    --mark-mid: #c9505f;
  }
  * { box-sizing: border-box; margin: 0; padding: 0; }
  html, body { width: 1200px; height: 1200px; overflow: hidden; }
  body {
    background: var(--page-bg);
    position: relative;
    font-family: "Montserrat", sans-serif;
  }
  .card {
    position: absolute;
    left: 130px;
    width: 940px;
    height: 535px;
    overflow: hidden;
    background: var(--card-red);
    box-shadow: 0 6px 18px rgba(0,0,0,0.18);
  }
  .card--front { top: 40px; }
  .card--back  { top: 625px; }

  .brand-name {
    position: absolute; left: 0; width: 100%;
    text-align: center;
    font-family: "Montserrat", sans-serif;
    font-weight: 500;
    text-transform: uppercase;
    letter-spacing: 5px;
    white-space: nowrap;
    line-height: 1;
  }

  /* front */
  .front__top {
    position: absolute; left: 0; top: 0;
    width: 100%; height: 197px;
    background: var(--card-white);
  }
  .front__brand { top: 58px; font-size: 26px; color: var(--logo-grey); }
  .front__mark {
    position: absolute; left: 298px; top: 112px;
    width: 343px; height: 129px;
    border-radius: 50%;
    background: radial-gradient(ellipse at 50% 50%, var(--mark-deep), var(--mark-mid) 55%, rgba(201,80,95,0) 72%);
  }
  .front__identity {
    position: absolute; left: 49px; top: 320px;
    width: 406px; text-align: right;
  }
  .person-name {
    display: block;
    text-align: left;
    font-weight: 700;
    font-size: 40px;
    line-height: 46px;
    letter-spacing: 1.2px;
    color: var(--blush);
    white-space: nowrap;
  }
  .person-role {
    display: block;
    margin-top: 4px;
    font-family: "Quicksand", sans-serif;
    font-size: 23px;
    line-height: 28px;
    color: var(--card-white);
  }
  .front__divider {
    position: absolute; left: 486px; top: 300px;
    width: 2px; height: 118px;
    background: rgba(255,255,255,0.55);
  }
  .contact-list {
    position: absolute; left: 537px; top: 287px;
    list-style: none;
  }
  .contact-list li {
    display: flex; align-items: center;
    height: 29px;
    font-weight: 600;
    font-size: 20px;
    color: var(--card-white);
    white-space: nowrap;
  }
  .contact-list .dot {
    width: 20px; height: 20px; border-radius: 50%;
    background: var(--card-white);
    margin-right: 11px; flex: none;
  }
  .contact-list svg { margin-right: 11px; flex: none; }
  .front__waves {
    position: absolute; left: 0; bottom: 0;
    width: 940px; height: 70px;
  }

  /* back */
  .back__mark {
    position: absolute; left: 390px; top: 210px;
    width: 160px; height: 58px;
    border-radius: 50%;
    background: radial-gradient(ellipse at center, rgba(255,255,255,0.85), rgba(255,255,255,0.25) 60%, rgba(255,255,255,0) 75%);
  }
  .back__brand { top: 294px; font-size: 28px; color: var(--card-white); }
  .back__url {
    position: absolute; left: 0; width: 100%; top: 506px;
    text-align: center;
    font-family: "Quicksand", sans-serif;
    font-size: 21px;
    line-height: 24px;
    color: var(--blush);
    letter-spacing: 0.3px;
  }
</style>
</head>
<body>

<section class="card card--front">
  <div class="front__top"></div>
  <div class="front__brand brand-name">Otter Tea Mug</div>
  <div class="front__mark" role="img" aria-label="Brand emblem illustration made of small berry-coloured circles"></div>

  <div class="front__identity">
    <span class="person-name">DORIAN FENWICK</span>
    <span class="person-role">Owner</span>
  </div>
  <div class="front__divider"></div>

  <ul class="contact-list">
    <li>
      <svg width="20" height="20" viewBox="0 0 20 20" aria-hidden="true">
        <circle cx="10" cy="10" r="10" fill="#fff"/>
        <path d="M6.5 5.2l2 0 .9 2.4-1.3.9c.7 1.4 1.8 2.5 3.2 3.2l.9-1.3 2.4.9 0 2c0 .6-.5 1-1.1 1C9.2 14.1 5.9 10.8 5.5 6.3c0-.6.4-1.1 1-1.1z" fill="var(--card-red)"/>
      </svg>317-594-8126
    </li>
    <li><span class="dot"></span>dorian.brews</li>
    <li><span class="dot"></span>otter_brew</li>
    <li><span class="dot"></span>dorian.brews</li>
    <li><span class="dot"></span>dorian.brews</li>
  </ul>

  <svg class="front__waves" viewBox="0 0 940 70" preserveAspectRatio="none" aria-hidden="true">
    <path d="M0 38 C180 8 380 22 560 50 C700 68 850 48 940 22 L940 70 L0 70 Z" fill="var(--blush)"/>
    <path d="M0 30 C110 14 240 12 330 20 C220 20 100 34 0 50 Z" fill="var(--card-white)"/>
    <path d="M0 56 C200 28 400 40 560 58 C700 70 840 58 940 34 L940 70 L0 70 Z" fill="var(--blush)" opacity="0.9"/>
    <path d="M860 30 C890 25 915 18 940 10 L940 16 C915 24 890 30 860 30 Z" fill="var(--card-white)"/>
  </svg>
</section>

<section class="card card--back">
  <div class="back__mark" role="img" aria-label="Small white brand emblem illustration"></div>
  <div class="back__brand brand-name">Otter Tea Mug</div>
  <div class="back__url">www.theottertyeamug.example</div>
</section>

</body>
</html>
```